Postcard - Promoting Wendell Ridge Brokers for Farm Clients

We need to develop a postcard (4" X 6") to send out to Agricultural clients.

The content on the email will be:

We understand that farming has variety of risk exposures that can affect your farm and your family’s future.
Wendell Ridge Brokers can help you identify and manage those risks by building an insurance program that works for you, your family and your operation. We ensure we understand your risk, you understand your coverage and we sort through the “fine” print together before a loss happens.
Contact Wendell Ridge Brokers to arrange a review and meet our team. 1-800-555-0147 farmteam@wendellridge.ca

Target Market(s)

We would like 2 separate postcards - one for crop farmers and one for cattle farmers

Industry/Entity Type

Agriculture

Requirements
Must have
• Be remarkable - something that catches your eye, and must have our logo

Please note that this can be 2 sided - potential to have the photo/color side to be the picture and some wording to catch the attention of the individual receiving .... and the back side to be the additional content, which is in the project description.

```html
<!DOCTYPE html>
<html lang="en">
<head>
<meta charset="utf-8">
<title>Wendell Ridge Brokers – Farm Postcards</title>
<link rel="stylesheet" href="https://fonts.googleapis.com/css2?family=Mulish:wght@400;800;900&family=Alegreya+Sans:wght@400;500;700&display=swap">
<style>
  :root {
    --page: #e8e8e8;
    --navy: #1f2a5c;
    --navy-deep: #1a2350;
    --accent-blue: #2f4fa8;
    --white: #ffffff;
    --stripe: #d9d9d9;
    --stamp: #d6d6d6;
    --rule: #3b4a7a;
    --shadow: rgba(0, 0, 0, 0.22);
  }
  * { box-sizing: border-box; margin: 0; padding: 0; }
  html, body {
    width: 1200px;
    height: 2240px;
    overflow: hidden;
    background: var(--page);
  }
  body { position: relative; font-family: "Alegreya Sans", sans-serif; }

  .postcard {
    position: absolute;
    left: 142px;
    width: 917px;
    height: 612px;
    box-shadow: 3px 4px 6px var(--shadow);
  }
  .postcard--livestock { top: 141px; }
  .postcard--back { top: 814px; }
  .postcard--crop { top: 1484px; }

  /* Front */
  .postcard--front { background: var(--navy); }
  .front-photo {
    position: absolute;
    left: 24px; top: 23px; right: 24px; bottom: 25px;
    clip-path: polygon(32px 0, 100% 0, 100% calc(100% - 26px), calc(100% - 26px) 100%, 0 100%, 0 32px);
  }
  .front-photo--sheep {
    background:
      radial-gradient(ellipse 22% 38% at 38% 62%, #b8aea0 0%, #8f8578 55%, rgba(80,70,60,0) 100%),
      radial-gradient(ellipse 25% 30% at 8% 10%, #d8dde4 0%, rgba(200,205,210,0) 100%),
      linear-gradient(115deg, #5d5852 0%, #4a403a 40%, #3a2f29 65%, #6b6258 100%);
  }
  .front-photo--wheat {
    background:
      linear-gradient(180deg, #eef0f3 0%, #e6e6e2 38%, #cdbf9a 55%, #a88f5c 75%, #6f6a3c 100%);
  }

  .headline {
    position: absolute;
    font-family: "Mulish", sans-serif;
    line-height: 1;
    white-space: nowrap;
  }
  .headline--light { color: var(--white); }
  .headline--dark { color: var(--navy); }
  .headline__line { position: absolute; right: 0; }
  .headline__line--1 { font-size: 66px; font-weight: 400; right: 122px; top: 48px; letter-spacing: -0.5px; }
  .headline__line--2 { font-size: 66px; font-weight: 400; right: 122px; top: 104px; letter-spacing: -0.5px; }
  .headline__line--2 strong { font-weight: 900; }
  .headline__line--3 { font-size: 70px; font-weight: 900; right: 50px; top: 178px; letter-spacing: 1px; }
  .headline { left: 0; top: 0; right: 0; bottom: 0; }

  .brand {
    position: absolute;
    display: flex;
    align-items: center;
    gap: 10px;
    font-family: "Alegreya Sans", sans-serif;
    font-weight: 700;
    text-transform: uppercase;
    letter-spacing: 0.5px;
  }
  .brand__dot {
    width: 40px; height: 40px;
    border-radius: 50%;
    flex: none;
  }
  .brand--front { left: 40px; bottom: 52px; color: var(--white); font-size: 22px; }
  .brand--front .brand__dot { background: var(--white); }

  .front-contact {
    position: absolute;
    right: 46px;
    bottom: 44px;
    font-family: "Alegreya Sans", sans-serif;
    font-weight: 700;
    font-size: 23px;
    color: var(--white);
    white-space: nowrap;
  }
  .front-contact__sep { margin: 0 8px; font-weight: 400; }

  /* Back */
  .postcard--back { background: var(--white); border: 1px solid #bdbdbd; }
  .back-shapes { position: absolute; left: 0; top: 0; width: 915px; height: 610px; }
  .brand--back { left: 46px; top: 50px; color: var(--navy); font-size: 26px; }
  .brand--back .brand__dot { background: var(--navy); width: 46px; height: 46px; }

  .back-intro {
    position: absolute;
    left: 46px; top: 124px;
    width: 432px;
    font-size: 18.5px;
    line-height: 23px;
    color: var(--navy);
    text-align: justify;
  }
  .back-intro strong { font-weight: 700; }
  .back-promise {
    position: absolute;
    left: 83px; top: 282px;
    width: 360px;
    font-size: 20px;
    line-height: 25.5px;
    font-weight: 700;
    color: var(--white);
  }
  .back-contact {
    position: absolute;
    left: 54px; top: 436px;
    color: var(--navy);
    font-weight: 700;
    font-size: 23px;
  }
  .back-contact__row { display: flex; align-items: center; gap: 10px; height: 35px; }
  .back-contact__icon { width: 20px; height: 20px; flex: none; }
  .back-cta {
    position: absolute;
    left: 53px; top: 514px;
    width: 298px; height: 54px;
    border: 1.5px dashed var(--accent-blue);
    padding: 6px 12px;
    font-size: 16px;
    line-height: 17px;
    color: var(--accent-blue);
  }
  .back-cta strong { font-weight: 700; }
  .stamp-box {
    position: absolute;
    left: 753px; top: 48px;
    width: 120px; height: 136px;
    background: var(--stamp);
  }
  .address-line {
    position: absolute;
    left: 554px; width: 332px;
    border-top: 1.5px solid var(--rule);
  }
</style>
</head>
<body>

<section class="postcard postcard--front postcard--livestock">
  <div class="front-photo front-photo--sheep" role="img" aria-label="Photo of young sheep in a barn, one looking toward the camera"></div>
  <h2 class="headline headline--light">
    <span class="headline__line headline__line--1">Have you</span>
    <span class="headline__line headline__line--2">got <strong>us</strong></span>
    <span class="headline__line headline__line--3">COVERED?</span>
  </h2>
  <div class="brand brand--front"><span class="brand__dot"></span>Wendell Ridge Brokers</div>
  <p class="front-contact">1-800-555-0147<span class="front-contact__sep">/</span>farmteam@wendellridge.ca</p>
</section>

<section class="postcard postcard--back">
  <svg class="back-shapes" viewBox="0 0 915 610" aria-hidden="true">
    <polygon points="0,0 565,0 500,265 0,265" fill="#cfd1d6"/>
    <polygon points="0,0 565,0 520,180 0,180" fill="#e3e4e7" opacity="0.6"/>
    <polygon points="0,265 500,265 463,415 0,415" fill="var(--navy)"/>
    <polygon points="565,0 580,0 432,610 417,610" fill="var(--stripe)"/>
  </svg>
  <div role="img" aria-label="Faded photo of a round hay bale in a harvested field" style="position:absolute;left:0;top:0;width:1px;height:1px;"></div>

  <div class="brand brand--back"><span class="brand__dot"></span>Wendell Ridge Brokers</div>

  <p class="back-intro">We understand that farming has variety of risk exposures that can affect your farm and your family’s future. <strong>Wendell Ridge Brokers</strong> can help you identify and manage those risks by building an insurance program that works for you, your family and your operation.</p>

  <p class="back-promise">We ensure we understand your risk, you understand your coverage and we sort through the “fine” print together before a loss happens.</p>

  <div class="back-contact">
    <div class="back-contact__row">
      <svg class="back-contact__icon" viewBox="0 0 24 24" aria-hidden="true"><path fill="var(--accent-blue)" d="M6.6 10.8a15.1 15.1 0 0 0 6.6 6.6l2.2-2.2a1 1 0 0 1 1-.25 11.4 11.4 0 0 0 3.6.57 1 1 0 0 1 1 1V20a1 1 0 0 1-1 1A17 17 0 0 1 3 4a1 1 0 0 1 1-1h3.5a1 1 0 0 1 1 1c0 1.25.2 2.45.57 3.57a1 1 0 0 1-.25 1z"/></svg>
      <span>1-800-555-0147</span>
    </div>
    <div class="back-contact__row">
      <svg class="back-contact__icon" viewBox="0 0 24 24" aria-hidden="true"><path fill="var(--accent-blue)" d="M2 5h20v14H2z"/><path fill="none" stroke="#fff" stroke-width="2" d="M2 6l10 7 10-7"/></svg>
      <span>farmteam@wendellridge.ca</span>
    </div>
  </div>

  <p class="back-cta">Contact <strong>Wendell Ridge Brokers</strong> to arrange a review and meet our team.</p>

  <div class="stamp-box"></div>
  <div class="address-line" style="top:364px;"></div>
  <div class="address-line" style="top:430px;"></div>
  <div class="address-line" style="top:496px;"></div>
  <div class="address-line" style="top:562px;"></div>
</section>

<section class="postcard postcard--front postcard--crop">
  <div class="front-photo front-photo--wheat" role="img" aria-label="Photo of ripe wheat heads in a field under a pale sky"></div>
  <h2 class="headline headline--dark">
    <span class="headline__line headline__line--1">Have you</span>
    <span class="headline__line headline__line--2">got <strong>us</strong></span>
    <span class="headline__line headline__line--3">COVERED?</span>
  </h2>
  <div class="brand brand--front"><span class="brand__dot"></span>Wendell Ridge Brokers</div>
  <p class="front-contact">1-800-555-0147<span class="front-contact__sep">/</span>farmteam@wendellridge.ca</p>
</section>

</body>
</html>
```